Shipping and Logistics, Project

Project description : Company Profile

A total logistics company covering domestic / international freight forwarding, warehouse management services, haulage, supply chain management, transport management & distribution, procurement & assembly services, shipping, chartering & bunker services, project logistics & tax exemption consultancy, oil & gas logistics, halal logistics services & integrated logistics management. We’re a well-established and experienced freight forwarder in Kuala Lumpur, Malaysia. We specialize in customized value-added solution that optimizes your supply chain by trimming inventory, reducing logistics cost and enhancing your customer service levels.

As a member of the Worldwide Carrier and Haulage Alliance which comprise of 170 global freight agents in 80 countries that promotes great handling in cross-trade logistics and freighting. You could rely on our efficiency in handlings of export cargo (FCL, LCL, Bulk and Conventional) between our global network offices worldwide with a total scale of 10,000 groomed specialists in various logistics division working together to ensure delivery task meets with your expectation. With our dedicated qualified and experienced professionals, we are fully committed to serving our clients.

Our generic services are listed below for your reference:

• Air Freight
• Ocean Freight FCL & LCL
• Container Haulage
• Warehousing
• Transportation and Distribution within Malaysia and Thailand
• Cross-Border Road Line-hauls between Thailand, Malaysia, Singapore and Laos
• Customs Brokerage and Forwarding
• Project Cargo Freight Forwarding for setting up of new plants / factories and ad hoc heavy-lift
• Air-Sea-Road-Rail multi-modal options
• Import / Export / Storage / Documentation / Handling of DG / Hazmat
• Vessel and Aircraft Charters

Our Mission
Based on the motto “Quick, Reliable and Polite”, we are dedicated to upholding the following three points corporate philosophy:
1. Adhering to the principle that “the customer always comes first”.
2. Contributing to the development of the local community.
3. Making it our duty to be responsible and sincere.

Our Edge
• One-Stop Logistics Solutions
• Extensive Network Throughout Malaysia
• Highly Qualified and Experienced Pool of Professionals
• Comprehensive IT Solutions
• Innovative and Customer-focused Solutions
• Flexible and Consistent in Managing Exceptions
• Total Supply Chain Visibility

Target Market
1. We sell the logistics services to all the industry in Malaysia and Worldwide. (ONE Stop Logistics Solutions)

Competitor
1. RT Volmaren
2. Corvella Transport
3. Brandt + Osswig
4. VELIRO
5. TZQ
6. Farrowline
7. Ruma Logistics

Rules for Picking a Company Name
1. Unique and unforgettable
2. Avoid unusual spellings
3. Easy to pronounce and remember
4. Keep it simple
5. Make some sense
6. Give a clue

Rules for Picking a Company Logo
4. Keep it simple
5. Make some sense
6. Give a clue

1. Simplicity
2. Memorability
3. Originality
4. Modern Yet Timeless
5. Balance
6. Complementary
7. Versatility

Stationery Information
1. Company Name : Tepiandek Solutions Sdn Bhd
2. Company Registration : 2730518-W
3. Address : 14-07, Jalan Seroja Indah 5, Taman Bukit Seroja, 81300 Johor Bahru, Johor, Malaysia.
4. Name : Derek Tan
5. Position : Manager
6. Mobile No : (+6019) 4308127
7. Office No : (+607) 5129870
8. Fax No : Not Available
9. Email Address : derek.tan@tepiandek-freight.example
10. Web Domain : www.tepiandek-freight.example
11. Company Slogan : Be Globally Connected

Target Market(s)

Corporate Company

Industry/Entity Type

Shipping and Logistics Industry

Requirements
Must have
• Company Full Name : TEPIANDEK SOLUTIONS SDN. BHD.
Nice to have
• Keep it simple and unforgettable ...

```html
<!DOCTYPE html>
<html lang="en">
<head>
<meta charset="utf-8">
<title>Tepiandek Solutions Stationery</title>
<link href="https://fonts.googleapis.com/css2?family=Poppins:wght@400;500;600&display=swap" rel="stylesheet">
<style>
:root{
  --stage:#c8c8c8;
  --blue:#3b87c9;
  --blue-light:#5ab0ff;
  --ink:#262626;
  --paper:#ffffff;
  --text:#2b2b2b;
  --rule:#d6d6d6;
}
*{margin:0;padding:0;box-sizing:border-box}
html,body{width:1200px;height:900px;overflow:hidden}
body{background:var(--stage);font-family:'Poppins',sans-serif;position:relative;color:var(--text)}
.piece{position:absolute}
.brand{display:flex;align-items:center;gap:5px}
.brand-mark{background:var(--blue);flex:none}
.brand-name{font-weight:500;color:var(--blue);line-height:1;letter-spacing:.02em}
.brand-sub{font-weight:500;color:var(--ink);letter-spacing:.18em;line-height:1;margin-top:2px}

/* folder */
.folder{left:114px;top:145px;width:314px;height:435px;background:var(--ink);overflow:hidden}
.folder svg{position:absolute;left:0;top:0}
.folder .brand{position:absolute;left:105px;top:52px;gap:10px}
.folder .brand-mark{width:40px;height:40px}
.folder .brand-name{font-size:24px;color:#fff}
.folder .brand-sub{font-size:9px;color:#fff;letter-spacing:.2em;margin-top:5px}
.folder-slogan{position:absolute;left:0;width:314px;top:400px;text-align:center;color:#fff;font-size:9px;letter-spacing:.14em}

/* letterhead */
.letterhead{left:460px;top:154px;width:291px;height:425px;background:var(--paper)}
.letterhead .brand{position:absolute;left:24px;top:14px}
.letterhead .brand-mark{width:18px;height:18px}
.letterhead .brand-name{font-size:11px}
.letterhead .brand-sub{font-size:4px}
.contact{position:absolute;right:19px;top:14px;text-align:right;font-size:5.2px;line-height:1.15}
.contact a{color:var(--blue);text-decoration:none}
.contact .address{margin-top:5px}
.letter-rule{position:absolute;left:19px;top:52px;width:185px;height:1px;background:var(--rule)}
.footer{position:absolute;left:0;bottom:0;width:100%;display:flex;align-items:center;color:#fff}
.footer-dark{background:var(--ink);height:100%}
.footer-band{flex:1;background:var(--blue);height:100%;display:flex;align-items:center;justify-content:space-between}
.footer-badge{width:14px;height:14px;background:#fff;border:2px solid var(--blue);flex:none;margin:0 4px}
.letterhead .footer{height:16px}
.letterhead .footer-dark{width:45px}
.letterhead .footer-band{font-size:6px;padding:0 21px 0 4px}

/* tall envelope */
.envelope-tall{left:786px;top:94px;width:307px;height:488px}
.envelope-tall .flap{position:absolute;left:0;top:0}
.envelope-tall .body{position:absolute;left:0;top:57px;width:307px;height:431px;background:var(--paper)}
.envelope-tall .brand{position:absolute;left:25px;top:37px}
.envelope-tall .brand-mark{width:18px;height:18px}
.envelope-tall .brand-name{font-size:11px}
.envelope-tall .brand-sub{font-size:4px}
.envelope-tall .footer{height:14px}
.envelope-tall .footer-dark{width:28px}
.envelope-tall .footer-band{font-size:5.2px;padding-left:2px}

/* DL envelope */
.envelope-dl{left:436px;top:624px;width:340px;height:196px}
.envelope-dl .flap{position:absolute;left:0;top:0}
.envelope-dl .body{position:absolute;left:0;top:26px;width:340px;height:170px;background:var(--paper)}
.envelope-dl .brand{position:absolute;left:17px;top:23px}
.envelope-dl .brand-mark{width:18px;height:18px}
.envelope-dl .brand-name{font-size:10px}
.envelope-dl .brand-sub{font-size:3.6px}
.return-address{position:absolute;left:19px;top:138px;font-size:5.6px;line-height:1.15}
</style>
</head>
<body>

<section class="piece folder">
  <svg width="314" height="435" viewBox="0 0 314 435">
    <defs>
      <linearGradient id="folderTone" x1="0" y1="0" x2="1" y2="1">
        <stop offset="0" stop-color="#3a86c8"/>
        <stop offset="1" stop-color="#3479b8"/>
      </linearGradient>
    </defs>
    <polygon points="0,0 125,0 0,75" fill="var(--blue)"/>
    <polygon points="0,66 125,0 0,75" fill="var(--blue-light)"/>
    <path d="M0,186 Q170,270 314,331 L314,435 L0,435 Z" fill="url(#folderTone)" role="img" aria-label="Blue field with a soft geometric texture"/>
    <path d="M0,186 Q170,270 314,331" fill="none" stroke="var(--blue-light)" stroke-width="3"/>
  </svg>
  <div class="brand">
    <span class="brand-mark"></span>
    <div>
      <div class="brand-name">TEPIANDEK</div>
      <div class="brand-sub">SOLUTIONS SDN. BHD.</div>
    </div>
  </div>
  <p class="folder-slogan">BE GLOBALLY CONNECTED</p>
</section>

<section class="piece letterhead">
  <div class="brand">
    <span class="brand-mark"></span>
    <div>
      <div class="brand-name">TEPIANDEK</div>
      <div class="brand-sub">SOLUTIONS SDN. BHD.</div>
    </div>
  </div>
  <div class="contact">
    <p>(+6019) 430 8127, (+607) 512 9870</p>
    <p>derek.tan@tepiandek-freight.example</p>
    <p>www.<a>tepiandek-freight</a>.example</p>
    <div class="address">
      <p>14-07, Jalan Seroja Indah 5</p>
      <p>Taman Bukit Seroja, 81300 Johor</p>
      <p>Bahru, Johor, Malaysia.</p>
    </div>
  </div>
  <div class="letter-rule"></div>
  <div class="footer">
    <div class="footer-dark"></div>
    <div class="footer-band">
      <span style="display:flex;align-items:center"><span class="footer-badge"></span><span style="margin-left:6px">BE GLOBALLY CONNECTED</span></span>
      <span>Company No. 2730518-W</span>
    </div>
  </div>
</section>

<section class="piece envelope-tall">
  <svg class="flap" width="307" height="60" viewBox="0 0 307 60">
    <polygon points="32,0 269,0 307,52 307,60 0,57 0,52" fill="var(--blue)"/>
  </svg>
  <div class="body">
    <div class="brand">
      <span class="brand-mark"></span>
      <div>
        <div class="brand-name">TEPIANDEK</div>
        <div class="brand-sub">SOLUTIONS SDN. BHD.</div>
      </div>
    </div>
    <div class="footer">
      <div class="footer-dark"></div>
      <div class="footer-band">
        <span style="display:flex;align-items:center"><span class="footer-badge"></span><span style="margin-left:4px">14-07, Jalan Seroja Indah 5, Taman Bukit Seroja, 81300 Johor Bahru, Johor, Malaysia.</span></span>
      </div>
    </div>
  </div>
</section>

<section class="piece envelope-dl">
  <svg class="flap" width="340" height="27" viewBox="0 0 340 27">
    <polygon points="15,0 322,0 340,26 0,26" fill="var(--blue)"/>
  </svg>
  <div class="body">
    <div class="brand">
      <span class="brand-mark"></span>
      <div>
        <div class="brand-name">TEPIANDEK</div>
        <div class="brand-sub">SOLUTIONS SDN. BHD.</div>
      </div>
    </div>
    <div class="return-address">
      <p>14-07, Jalan Seroja Indah 5,</p>
      <p>Taman Bukit Seroja, 81300 Johor</p>
      <p>Bahru, Johor, Malaysia.</p>
    </div>
  </div>
</section>

</body>
</html>
```